Plumbing and heating business card design

i need a new business card for the company i work for called Dr. Brightpipe. It is a plumbing and heating company that has been operating for over 30 years. We are not like these big plumbing companies that have ways to charge the customer as much as possible. Our company does only what is necessary and what is needed to do the job right the first time without the high cost. we are a neighborhood business which kind of explains why we don't charge customers through the roof. I would like to see a design with a nice background anything but just plain white. maybe like a light blue at the top of the design. on the back of the card i would like it to say " T. Vandermeer's Dr. Brightpipe". maybe add some color to the lettering on the front of the card for example blue font for plumbing and red font for heating. raised print. im sure Cardolux designers will make it look good. The final design should help spread a good word about our company and help grow business.

Industry/Entity Type

Business

Contact Information for Business Card

Dr. Brightpipe, Plumbing & heating, Gordon Tasker, Northeast District Operations manager, 4827 Birchwell st., Office:(555)-284-1937, doctorbrightpipe@mailverra.net

Requirements
Must have
• raised print finish and a nice sturdy feel.

```html
<!DOCTYPE html>
<html lang="en">
<head>
<meta charset="utf-8">
<title>Dr. Brightpipe Plumbing &amp; Heating – Business Card</title>
<link rel="stylesheet" href="https://fonts.googleapis.com/css2?family=Saira:wght@400;500;600;700&display=swap">
<style>
  :root {
    --page-bg: #ebecec;
    --card-white: #ffffff;
    --brand-blue: #1b6385;
    --title-blue: #1d5f82;
    --brand-red: #b8282c;
    --ink-light: #ffffff;
    --art-top: #e9eef2;
    --art-bottom: #cdd9e3;
  }
  * { margin: 0; padding: 0; box-sizing: border-box; }
  html, body {
    width: 980px; height: 1200px; overflow: hidden;
    background: var(--page-bg);
    font-family: "Saira", "Arial Narrow", sans-serif;
  }
  .canvas { position: relative; width: 980px; height: 1200px; }

  .card {
    position: absolute;
    box-shadow: 0 6px 18px rgba(0,0,0,0.18);
    overflow: hidden;
  }

  /* Front */
  .card-front {
    left: 84px; top: 84px; width: 806px; height: 479px;
    background: var(--card-white);
  }
  .mascot-art {
    position: absolute; left: 79px; top: 45px; width: 197px; height: 200px;
    background: linear-gradient(180deg, var(--art-top), var(--art-bottom));
  }
  .brand-name {
    position: absolute; left: 313px; top: 62px;
    font-size: 50px; font-weight: 700; line-height: 1;
    font-variant: small-caps; letter-spacing: 1px;
    color: var(--brand-red);
    white-space: nowrap;
  }
  .brand-services {
    position: absolute; left: 315px; top: 158px;
    font-size: 33px; font-weight: 600; line-height: 1;
    font-variant: small-caps; letter-spacing: 0.5px;
    color: var(--title-blue);
    white-space: nowrap;
  }
  .rule-red {
    position: absolute; left: 0; top: 246px; width: 100%; height: 4px;
    background: var(--brand-red);
  }
  .contact-band {
    position: absolute; left: 0; top: 253px; width: 100%; height: 226px;
    background: var(--brand-blue);
    color: var(--ink-light);
    font-variant: small-caps;
  }
  .person {
    position: absolute; right: 510px; top: 32px; text-align: right;
    white-space: nowrap;
  }
  .person-name {
    font-size: 27px; font-weight: 500; letter-spacing: 2.5px; line-height: 1;
  }
  .person-role {
    margin-top: 14px;
    font-size: 18px; font-weight: 500; letter-spacing: 2px; line-height: 28px;
  }
  .divider {
    position: absolute; left: 318px; top: 38px; width: 2px; height: 140px;
    background: var(--ink-light);
  }
  .contact-list { list-style: none; position: absolute; left: 344px; top: 0; }
  .contact-item {
    position: absolute; left: 0; display: flex; align-items: center;
    white-space: nowrap;
    font-size: 16px; font-weight: 500; letter-spacing: 1.8px;
  }
  .contact-item svg { width: 24px; height: 24px; margin-right: 12px; flex: none; }
  .item-phone { top: 40px; }
  .item-mail  { top: 66px; }
  .item-addr  { top: 104px; }
  .item-web   { top: 142px; }

  /* Back */
  .card-back {
    left: 88px; top: 613px; width: 804px; height: 476px;
    background: var(--brand-blue);
    color: var(--ink-light);
  }
  .back-title {
    position: absolute; left: 0; right: 0; top: 188px; text-align: center;
    font-size: 40px; font-weight: 600; letter-spacing: 1px;
    font-variant: small-caps; line-height: 1;
    white-space: nowrap;
  }
  .back-phone {
    position: absolute; left: 205px; top: 318px;
    display: flex; align-items: center;
    font-size: 35px; font-weight: 700; letter-spacing: 1px; line-height: 1;
  }
  .back-phone svg { width: 40px; height: 48px; margin-right: 8px; }
</style>
</head>
<body>
<main class="canvas">

  <section class="card card-front" aria-label="Business card front">
    <div class="mascot-art" role="img" aria-label="Illustration of a cheerful plumber in overalls holding a pipe wrench and a plunger"></div>
    <div class="brand-name">Dr. Brightpipe</div>
    <div class="brand-services">Plumbing&amp;Heating</div>
    <div class="rule-red"></div>

    <div class="contact-band">
      <div class="person">
        <div class="person-name">Gordon Tasker</div>
        <div class="person-role">Northeast&nbsp; District<br>Operations manager</div>
      </div>
      <div class="divider"></div>
      <ul class="contact-list">
        <li class="contact-item item-phone">
          <svg viewBox="0 0 24 24" aria-hidden="true"><path fill="none" stroke="#fff" stroke-width="1.8" stroke-linejoin="round" d="M7 3l3 5-2 2c1 2.5 3.5 5 6 6l2-2 5 3-2 4C11 21 3 13 3 5z"/></svg>
          (555)-284-1937
        </li>
        <li class="contact-item item-mail">
          <svg viewBox="0 0 24 24" aria-hidden="true"><rect x="3" y="6" width="18" height="12" fill="none" stroke="#fff" stroke-width="1.8"/><path d="M3 6l9 7 9-7" fill="none" stroke="#fff" stroke-width="1.8"/></svg>
          doctorbrightpipe@mailverra.net
        </li>
        <li class="contact-item item-addr">
          <svg viewBox="0 0 24 24" aria-hidden="true"><path d="M3 11l9-7 9 7" fill="none" stroke="#fff" stroke-width="2"/><rect x="5" y="11" width="14" height="9" fill="none" stroke="#fff" stroke-width="2"/><line x1="12" y1="11" x2="12" y2="20" stroke="#fff" stroke-width="2"/></svg>
          4827 Birchwell St.,Philadelphia
        </li>
        <li class="contact-item item-web">
          <svg viewBox="0 0 24 24" aria-hidden="true"><rect x="3" y="3" width="18" height="18" rx="3" fill="none" stroke="#fff" stroke-width="1.8"/></svg>
          www.neighborlink.net/doctorbrightpipe
        </li>
      </ul>
    </div>
  </section>

  <section class="card card-back" aria-label="Business card back">
    <div class="back-title">T. Vandermeer's Dr. Brightpipe</div>
    <div class="back-phone">
      <svg viewBox="0 0 20 24" aria-hidden="true"><path fill="#fff" d="M5 1l3 6-2 2c.5 3 2.5 6 5 8l2-1.5 4 4-2.5 3.5C7 22 1 13 1.5 4z"/></svg>
      (555)-284-1937
    </div>
  </section>

</main>
</body>
</html>
```